New look while maintaining the Brand identification!

I want a new look for my business card. I want to keep the same colors and feel but change the look and layout a bit. The logo (KALMORETIX Physical therapy Reimagined and the lilypad) must remain the same and in that font.
We are a physical therapy clinic. So we have certification that we can write on the back or services we provide (which is what we currently have on the back of the card as well)

Contact information
2840 Cedar Hollow Rd., #22
Naples, FL 34276
P: (239) 555-0172
F: (239) 555-0198
E: kalmoretixcare@mailvexo.com
W: www.kalmoretixcare-example.com

Industry/Entity Type

Physical Therapy

Contact Information for Business Card

Our current cards have the business address and information on the back. But I am willing to have it be in the front.

Font styles to use
Sans Serif

Colors
abd036
fbf289
ec1f27

Requirements
Must have
• Has to be unique!
• Services we provide and/or techniques we do must fit on the card
Nice to have
• Would like to have the front and back somehow linked together. Such that if you set the front next to the back, there is a nice flow of design! Currently the back is white with writing on it.
Should not have
• I like the wave lines as compared to straight lines.

```html
<!DOCTYPE html>
<html lang="en">
<head>
<meta charset="utf-8">
<title>Kalmoretix Business Card</title>
<link href="https://fonts.googleapis.com/css2?family=Open+Sans:wght@400;600;700&display=swap" rel="stylesheet">
<style>
  :root {
    --red: #ec1f27;
    --green: #abd036;
    --cream: #fbf289;
    --mustard: #c8b22e;
    --white: #ffffff;
    --table: #efe6d6;
  }
  html, body {
    margin: 0;
    width: 1200px;
    height: 960px;
    overflow: hidden;
    background: var(--table);
    font-family: "Open Sans", Arial, sans-serif;
  }
  .card {
    position: absolute;
    left: 250px;
    width: 700px;
    height: 400px;
    background: var(--white);
    box-shadow: 0 8px 24px rgba(0,0,0,0.18);
  }
  .card-front { top: 50px; }
  .card-back { top: 510px; }

  /* Front */
  .front-panel {
    position: absolute;
    inset: 28px;
    background: var(--red);
    border-radius: 22px;
  }
  .accent-square {
    position: absolute;
    width: 64px;
    height: 64px;
    background: var(--green);
  }
  .accent-top { left: 120px; top: 0; }
  .accent-bottom { left: 300px; bottom: 0; }
  .front-name {
    position: absolute;
    left: 28px;
    top: 0;
    width: 300px;
    height: 100%;
    display: flex;
    align-items: center;
    justify-content: center;
    color: var(--cream);
    font-weight: 700;
    font-size: 30px;
    letter-spacing: 1px;
  }
  .divider {
    position: absolute;
    left: 340px;
    top: 90px;
    width: 1px;
    height: 260px;
    background: rgba(255,255,255,0.45);
  }
  .contact {
    position: absolute;
    left: 370px;
    top: 110px;
    color: var(--white);
    font-size: 17px;
    line-height: 1.35;
  }
  .contact p { margin: 0; }
  .contact .phones {
    margin: 10px 0;
    font-size: 27px;
    line-height: 1.2;
  }
  .contact .web { font-size: 16px; }

  /* Back */
  .back-frame {
    position: absolute;
    inset: 24px;
    border: 2px solid var(--red);
    border-radius: 22px;
  }
  .back-square {
    position: absolute;
    left: 318px;
    top: 0;
    width: 64px;
    height: 64px;
    background: var(--red);
  }
  .back-name {
    position: absolute;
    left: 0;
    right: 0;
    top: 120px;
    text-align: center;
    color: var(--mustard);
    font-weight: 700;
    font-size: 56px;
    letter-spacing: 1px;
  }
  .services-title {
    position: absolute;
    left: 0;
    right: 0;
    top: 236px;
    text-align: center;
    color: var(--red);
    font-size: 14px;
    letter-spacing: 5px;
  }
  .services-rule {
    position: absolute;
    left: 60px;
    right: 60px;
    top: 276px;
    height: 1px;
    background: var(--red);
  }
  .services-list {
    position: absolute;
    left: 60px;
    right: 60px;
    top: 296px;
    display: flex;
    justify-content: space-between;
    color: var(--green);
    font-size: 20px;
    letter-spacing: 1.5px;
  }
</style>
</head>
<body>
  <section class="card card-front">
    <div class="front-panel"></div>
    <div class="accent-square accent-top"></div>
    <div class="accent-square accent-bottom"></div>
    <div class="front-name">KALMORETIX</div>
    <div class="divider"></div>
    <div class="contact">
      <p>2840 Cedar Hollow Rd., #22</p>
      <p>Naples, FL 34276</p>
      <p class="phones">(239) 555-0172<br>(239) 555-0198</p>
      <p class="web">kalmoretixcare@mailvexo.com</p>
      <p class="web">www.kalmoretixcare-example.com</p>
    </div>
  </section>

  <section class="card card-back">
    <div class="back-frame"></div>
    <div class="back-square"></div>
    <div class="back-name">KALMORETIX</div>
    <div class="services-title">OUR SERVICES</div>
    <div class="services-rule"></div>
    <div class="services-list">
      <span>OUR SERVICES</span>
      <span>OUR SERVICES</span>
      <span>OUR SERVICES</span>
    </div>
  </section>
</body>
</html>
```